Need website redesign!

I have a site, www.pinebrookfitcamp.com

I am looking to have it redesigned to make it simpler, and encourage people who hit the home page to click on a service, opt in, or contact me for more info. Having a video front and center with icons representing the services we offer around it may be a good idea, but I am open to YOUR design. Conversion is my goal. I want it to be friendly, but convey the fun and ENERGY of my bootcamp. Scrolling pics on home page so people can get a feel for our bootcamp is recommended as well.

```html
<!DOCTYPE html>
<html lang="en">
<head>
<meta charset="utf-8">
<title>Blaze Fit Camp</title>
<link href="https://fonts.googleapis.com/css2?family=Open+Sans:wght@300;400;600;700&display=swap" rel="stylesheet">
<style>
:root{
  --black:#000;
  --dark:#1c1c1c;
  --darker:#141414;
  --red:#d01517;
  --red-text:#e02020;
  --white:#fff;
  --muted:#b5b5b5;
  --footer-text:#8d8d8d;
  --button-top:#e9e9e9;
  --button-bottom:#bdbdbd;
}
*{box-sizing:border-box;margin:0;padding:0}
html,body{width:690px;height:1200px;overflow:hidden;background:var(--dark);font-family:'Open Sans',sans-serif;color:var(--white)}
.page{position:relative;width:690px;height:1200px}
.abs{position:absolute}
.btn{position:absolute;background:linear-gradient(var(--button-top),var(--button-bottom));color:#444;font-weight:600;text-transform:uppercase;text-align:center;border:1px solid #999;border-radius:2px;font-size:7px;letter-spacing:.2px;white-space:nowrap}
.red{color:var(--red-text)}

.site-header{left:0;top:0;width:690px;height:62px;background:var(--black)}
.brand{left:62px;top:10px;font-weight:700;font-size:14px;line-height:14px;color:var(--red);text-transform:uppercase;width:70px}
.brand-url{left:66px;top:50px;font-size:4px;color:var(--white);letter-spacing:.2px}
.main-nav{right:45px;top:41px;display:flex;gap:37px;font-size:6.2px;text-transform:uppercase;letter-spacing:.3px}
.promo-bar{left:0;top:62px;width:690px;height:36px;background:var(--red);font-size:6.6px;font-weight:600;text-align:center;line-height:36px;text-transform:uppercase;white-space:nowrap}

.hero{left:0;top:98px;width:690px;height:247px;background:linear-gradient(100deg,#a9bfd3 0%,#d8c4bd 35%,#8c8a98 60%,#c9ccd6 100%)}
.slide-arrow{top:205px}
.optin{left:475px;top:133px;width:158px;height:185px;background:var(--red);text-align:center}
.optin h2{font-size:8.4px;font-weight:700;line-height:14px;text-transform:uppercase;margin-top:14px}
.field{position:absolute;left:14px;width:130px;height:19px;background:#b81214;border:1px solid #a50f11;font-size:5px;text-align:left;padding:6px 7px}
.optin .note{position:absolute;left:0;top:145px;width:158px;font-size:5.4px;line-height:11px;text-transform:uppercase}

.welcome{left:0;top:345px;width:690px;height:86px;background:var(--darker);text-align:center}
.welcome h1{font-size:11.5px;font-weight:700;margin-top:20px;text-transform:uppercase}
.welcome p{font-size:6px;line-height:14.5px;color:var(--muted);width:520px;margin:6px auto 0}

.video{left:57px;top:459px;width:210px;height:145px;background:linear-gradient(135deg,#333 0%,#6b6057 50%,#222 100%)}
.video-bar{left:57px;top:594px;width:210px;height:10px;background:#111}
.about{left:294px;top:459px;width:170px}
.about h2{font-size:10px;font-weight:700;line-height:15px;text-transform:uppercase}
.about p{font-size:5.4px;line-height:12.8px;color:var(--muted);margin-top:6px}
.booking{left:480px;top:459px;width:153px;height:146px;background:linear-gradient(135deg,#c9c2c8,#8d8ea6)}
.booking .t1{position:absolute;left:20px;top:75px;font-size:10px;font-weight:700;color:#111}
.booking .t2{position:absolute;left:20px;top:87px;font-size:15px;font-weight:300;color:var(--white);text-transform:uppercase}

.feature{left:57px;top:643px;width:576px;height:212px;background:linear-gradient(90deg,#c7c7c7,#9a8f8c)}
.feature-panel{left:57px;top:643px;width:202px;height:212px;background:linear-gradient(#2c2c2c,#1a1a1a)}
.feature-panel h2{position:absolute;left:27px;top:23px;font-size:15px;font-weight:700;color:var(--red-text);text-transform:uppercase}
.feature-panel h3{position:absolute;left:27px;top:40px;font-size:23px;font-weight:300;text-transform:uppercase}
.feature-panel p{position:absolute;left:27px;top:79px;width:160px;font-size:5.6px;line-height:13.8px;color:#ddd}

.section-title{font-size:10.5px;font-weight:700;text-transform:uppercase}
.thumb{width:72px;height:72px;border-radius:50%;border:2px solid #fff}
.card-text{font-size:5.6px;line-height:12.5px;color:#ddd;width:185px}
.card-text .head{text-transform:uppercase;font-weight:600}
.card-text .meta{color:var(--red-text);font-style:italic}

.site-footer{left:0;top:1012px;width:690px;height:160px;background:var(--darker)}
.col{position:absolute;top:26px;font-size:5.2px;line-height:13px;color:var(--footer-text);text-transform:uppercase}
.col h4{font-size:6.6px;color:var(--white);font-weight:700;margin-bottom:6px}
.social{display:flex;align-items:center;gap:6px;margin-bottom:6px}
.social span.box{width:14px;height:14px;border:1px solid #666;display:inline-block}
.copyright{left:0;top:1172px;width:690px;height:28px;background:#0b0b0b;font-size:5px;color:var(--footer-text);text-align:center;line-height:28px;text-transform:uppercase}
</style>
</head>
<body>
<div class="page">

  <header class="abs site-header">
    <div class="abs brand">Blaze Fit Camp</div>
    <div class="abs brand-url">PINEBROOKFITCAMP.COM</div>
    <div class="btn" style="left:446px;top:11px;width:76px;height:18px;line-height:16px">Members Login</div>
    <div class="btn" style="left:532px;top:11px;width:101px;height:18px;line-height:16px">New Members Register</div>
    <nav class="abs main-nav"><span>Home</span><span>Services</span><span>Classes</span><span>About Us</span><span>FAQ's</span><span>Contact Us</span></nav>
  </header>

  <div class="abs promo-bar">Check out the premier Lindale &amp; Cresthaven County bootcamp designed to help you lose fat, get in incredible shape, and have a blast while doing it!</div>

  <div class="abs hero" role="img" aria-label="Smiling group doing sit-ups on exercise balls in a bright gym class"></div>
  <svg class="abs slide-arrow" style="left:18px" width="12" height="40"><polyline points="10,1 2,20 10,39" fill="none" stroke="#fff" stroke-width="1"/></svg>
  <svg class="abs slide-arrow" style="left:660px" width="12" height="40"><polyline points="2,1 10,20 2,39" fill="none" stroke="#fff" stroke-width="1"/></svg>

  <form class="abs optin">
    <h2>Leave your email for a<br>free week of bootcamp,<br>no obligation</h2>
    <div class="field" style="top:64px">Name :</div>
    <div class="field" style="top:90px">Email :</div>
    <div class="btn" style="left:27px;top:118px;width:104px;height:22px;line-height:20px;font-size:7px">Get Started Now!</div>
    <p class="note">Spam free zone.Your email is safe<br>&amp; secure.</p>
  </form>

  <section class="abs welcome">
    <h1>Welcome to <span class="red">Blaze Fit Camp</span></h1>
    <p>Blaze Fit Camp was started by longtime Lindale County resident Dale Rowan. Dale has been training individuals and small groups for more than 15 years and after one too many WET and COLD outdoor bootcamp workouts, Dale decided that INSIDE was the way to go.</p>
  </section>

  <div class="abs video" role="img" aria-label="Video still of a muscular trainer doing push-ups"></div>
  <svg class="abs" style="left:147px;top:517px" width="30" height="30"><rect width="30" height="30" rx="4" fill="#000" opacity=".45"/><polygon points="11,8 22,15 11,22" fill="#4a9fe0"/></svg>
  <div class="abs video-bar"></div>
  <svg class="abs" style="left:60px;top:595px" width="205" height="8"><rect x="1" y="1" width="1.5" height="6" fill="#aaa"/><rect x="4" y="1" width="1.5" height="6" fill="#aaa"/><text x="30" y="6" font-size="5" fill="#ccc" font-family="Open Sans,sans-serif">0:04 / 0:30</text><rect x="66" y="3" width="120" height="2" fill="#555"/><rect x="66" y="3" width="20" height="2" fill="#aaa"/><circle cx="70" cy="4" r="3" fill="#eee"/></svg>

  <div class="abs about">
    <h2>What is Blaze Fit<br><span class="red">Camp?</span></h2>
    <p>Blaze Fit Camp was started by longtime Lindale County resident Dale Rowan. Dale has been training individuals and small groups for more than 15 years and after one too many WET and COLD outdoor bootcamp workouts, Dale decided that INSIDE was the way to go.</p>
  </div>
  <div class="btn" style="left:294px;top:581px;width:104px;height:21px;line-height:19px">Get Started Now!</div>

  <div class="abs booking" role="img" aria-label="Women stretching in a bright fitness studio">
    <span class="t1">HAVE TO JOIN!</span>
    <span class="t2">For Booking</span>
    <div class="btn" style="left:20px;top:111px;width:114px;height:20px;line-height:18px">Members Book Now</div>
  </div>

  <div class="abs feature" role="img" aria-label="Woman in a pink top doing a plank workout"></div>
  <div class="abs feature-panel">
    <h2>No need to be</h2>
    <h3>Intimidated</h3>
    <p>No need to be intimidated, we want you to get started at a pace that is comfortable to you. Our goal is to help you reach YOUR goals and we do it in a fun, non-intimidating environment.</p>
    <div class="btn" style="left:27px;top:142px;width:104px;height:21px;line-height:19px">Get Started Now!</div>
    <svg class="abs" style="left:27px;top:175px" width="34" height="16"><rect width="15" height="15" fill="#d01517"/><rect x="17" width="15" height="15" fill="#d01517"/><polyline points="9,4 6,7.5 9,11" fill="none" stroke="#fff"/><polyline points="23,4 26,7.5 23,11" fill="none" stroke="#fff"/></svg>
  </div>

  <h2 class="abs section-title" style="left:56px;top:881px">Recent <span class="red">Posts</span></h2>
  <svg class="abs" style="left:304px;top:882px" width="12" height="8"><polyline points="3,1 1,4 3,7" fill="none" stroke="#999"/><polyline points="9,1 11,4 9,7" fill="none" stroke="#999"/></svg>
  <div class="abs thumb" style="left:56px;top:916px;background:linear-gradient(135deg,#7fb2c9,#9bd14a)" role="img" aria-label="Member stretching on a mat"></div>
  <div class="abs card-text" style="left:143px;top:919px">
    <div class="head">Our fun, effective workouts are designed to give you the maximum results.</div>
    <div class="meta">Posted on 27 November 2015</div>
    <div>Lorem Ipsum is simply dummy text of the printing and typesetting industry. has been the industry's...</div>
  </div>

  <h2 class="abs section-title" style="left:356px;top:881px">Happy <span class="red">Client's</span></h2>
  <svg class="abs" style="left:604px;top:882px" width="12" height="8"><polyline points="3,1 1,4 3,7" fill="none" stroke="#999"/><polyline points="9,1 11,4 9,7" fill="none" stroke="#999"/></svg>
  <div class="abs thumb" style="left:356px;top:916px;background:linear-gradient(135deg,#d9c6a8,#3f6a8a)" role="img" aria-label="Client portrait"></div>
  <div class="abs card-text" style="left:444px;top:919px;width:180px">
    <div class="head">Tessa Marlow</div>
    <div class="meta">Marketing Researcher</div>
    <div>Lorem Ipsum is simply dummy text of the printing and typesetting industry. has been the industry's simply dummy text of the printing and typesetting industry. has been the industry's...</div>
  </div>

  <footer class="abs site-footer">
    <div class="col" style="left:61px"><h4>Welcome</h4>Home<br>Services<br>Classes<br>About Us<br>FAQ's<br>Contact Us</div>
    <div class="col" style="left:144px"><h4>Services</h4>Boot Camp<br>Small Group Training<br>Personal Training<br>Specialty Training<br>Yoga<br>Kids Sports/Agility<br>Corporate Training</div>
    <div class="col" style="left:255px"><h4>Information</h4>Partners<br>Member<br>Partner Login</div>
    <div class="col" style="left:363px"><h4>Contact Us</h4>Ridgeview Martial Arts Studio<br>1180 Larkspur Lane Meadow Hall Building<br>Fernbrook 21990<br><span class="red">And</span><br>4420 Commerce Row Suite B Oakvale 21995</div>
    <div class="col" style="left:560px"><h4>Follow Us</h4>
      <div class="social"><span class="box"></span>: Friendwall</div>
      <div class="social"><span class="box"></span>: Chirpline</div>
      <div class="social"><span class="box"></span>: Searchcircle</div>
      <div class="social"><span class="box"></span>: Worklink</div>
      <div class="social"><span class="box"></span>: Clipstream</div>
    </div>
  </footer>
  <div class="abs copyright">© 2015. Blaze Fit Camp. All rights reserved.</div>

</div>
</body>
</html>
```